New Business Card Design*

We are a recruitment company based in Norwich/Cambridge England.
I have included our company logo which we want to remain the same.

What we are looking for is a new creative Business card which will really stand out!!

Contact Information for Business Card

Harriet Vance
email: Harriet@brelvix.co.uk
Address: Tolworth House
Ashgrove Innovation Park
Pelham Road
Norwich
KT9 3QD
Tel:01632 960418

```html
<!DOCTYPE html>
<html lang="en">
<head>
<meta charset="utf-8">
<title>Brelvix Business Card</title>
<link href="https://fonts.googleapis.com/css2?family=Montserrat:wght@500;600;700&display=swap" rel="stylesheet">
<style>
  :root {
    --backdrop: #a6a6a6;
    --brand-green: #97bf1a;
    --brand-grey: #8e8a8c;
    --card-white: #ffffff;
  }
  * { margin: 0; padding: 0; box-sizing: border-box; }
  html, body { width: 1200px; height: 900px; overflow: hidden; }
  body {
    background: var(--backdrop);
    font-family: "Montserrat", sans-serif;
    position: relative;
  }
  .card {
    position: absolute;
    top: 200px;
    width: 310px;
    height: 502px;
    border-radius: 28px;
    overflow: hidden;
  }
  .card-back {
    left: 265px;
    background: var(--brand-green);
    display: flex;
    align-items: center;
    justify-content: center;
  }
  .back-mark {
    display: flex;
    align-items: center;
    gap: 12px;
    color: var(--card-white);
    font-weight: 700;
    font-size: 34px;
  }
  .back-mark .dot {
    width: 30px; height: 30px; border-radius: 50%;
    background: var(--card-white);
  }
  .card-front {
    left: 641px;
    background: var(--card-white);
  }
  .brand {
    position: absolute;
    left: 15px;
    top: 26px;
    display: flex;
    align-items: center;
    gap: 10px;
  }
  .brand .dot {
    width: 40px; height: 40px; border-radius: 50%;
    background: var(--brand-green);
  }
  .brand-name {
    font-weight: 600;
    font-size: 29px;
    color: var(--brand-grey);
    line-height: 1;
  }
  .brand-tagline {
    font-weight: 600;
    font-size: 6px;
    letter-spacing: 1.1px;
    color: var(--brand-grey);
    margin-top: 2px;
  }
  .person-name {
    position: absolute;
    left: 15px;
    top: 305px;
    font-weight: 700;
    font-size: 20px;
    color: var(--brand-green);
    letter-spacing: 0.3px;
  }
  .info-band {
    position: absolute;
    left: 0; right: 0; bottom: 0;
    top: 327px;
    background: var(--brand-green);
    color: var(--card-white);
  }
  .person-role {
    position: absolute;
    left: 15px; top: 4px;
    font-weight: 600;
    font-size: 13.5px;
    letter-spacing: 0.4px;
  }
  .contact-list {
    position: absolute;
    left: 15px; top: 72px;
    list-style: none;
    font-weight: 600;
    font-size: 12px;
    line-height: 15px;
  }
  .social-list {
    position: absolute;
    left: 15px; right: 16px; top: 141px;
    list-style: none;
    display: flex;
    justify-content: space-between;
    font-weight: 600;
    font-size: 12px;
  }
  .social-list li { display: flex; align-items: center; gap: 6px; }
  .social-list .square {
    width: 11px; height: 11px;
    background: var(--card-white);
  }
</style>
</head>
<body>
  <section class="card card-back" aria-label="Card back">
    <div class="back-mark"><span class="dot"></span>Brelvix</div>
  </section>

  <section class="card card-front" aria-label="Card front">
    <div class="brand">
      <span class="dot"></span>
      <div>
        <div class="brand-name">Brelvix</div>
        <div class="brand-tagline">Technology Recruitment</div>
      </div>
    </div>

    <h1 class="person-name">YOUR NAME</h1>

    <div class="info-band">
      <p class="person-role">FOUNDER / CEO</p>
      <ul class="contact-list">
        <li>+1 555 010 4827</li>
        <li>yourname@brelvix.com</li>
        <li>www.brelvix.com</li>
      </ul>
      <ul class="social-list">
        <li><span class="square"></span>/brelvix</li>
        <li><span class="square"></span>/brelvix</li>
        <li><span class="square"></span>/brelvix</li>
      </ul>
    </div>
  </section>
</body>
</html>
```